Logo and metal business card design

Updated added my current logo which focus needs to be concentrated on. Have to have the new logo before the card. Company name is The Calder Works, LLC

Update: Reminder this is a Logo and business card design. I want the logo to be “CalderW” in a unique professional design that says secure, insurance, financial.

The G needs to be a P in the cut out

Update: the top two images have design on the metal which I am looking for

New black metal business cards. And CalderW.com logo that will go on the card. This will be a cut out design in the metal. Featuring “CalderW.com as the main cutout. Like the idea of .com to be separate or smaller and possible color. Looking for unique CalderW font design and a surrounding design per the examples below. Calder and G need to be different and the G a specific designing the mesh like the attached with the V in the mesh. But card side ways.. so mesh on right side of card with a G and .com in lower corner or where it fits Also looking to add my main info on the back side of the card. Derek M. Cell Email@mailbox-example.net We are an commercial insurance broker specializing in program business.
Updates

Need more time not enough entry’s and they are all the same.. I’m suppose to get 75 plus and not 20 that are the exact same from artist??? Need more submissions to compare. I committed my money so I do not want a refund I want more submissions from different artist

Target Market(s)

Insurance for the Restaurant industry

Industry/Entity Type

Insurance Broker

Contact Information for Business Card

New black metal business cards. And CalderW.com logo that will go on the card. This will be a cut out design in the metal. Featuring “CalderW.com as the main cutout. Like the idea of .com to be separate or smaller and possible color. Looking for unique CalderW font design and a surrounding design per the examples below. Calder and G need to be different and the G a specific designing the mesh like the attached with the V in the mesh. But card side ways.. so mesh on right side of card with a G and .com in lower corner or where it fits
Also looking to add my main info on the back side of the card.
Derek M.
Cell
Email@mailbox-example.net

We are an commercial insurance broker specializing in program business.

Logo Text

CalderW.com

Font styles to use
Decorative
Script
Other font styles liked:

Requirements
Must have
• Must have Calder and G distinctively different
Nice to have
• On flat parts I want texture on top of card

```html
<!DOCTYPE html>
<html lang="en">
<head>
<meta charset="UTF-8">
<title>The Calder Works – Metal Business Card</title>
<link rel="stylesheet" href="https://fonts.googleapis.com/css2?family=Montserrat:wght@400;500;600&display=swap">
<style>
  :root {
    --stage: #2c568c;
    --metal: #151617;
    --metal-edge: #2a2c2f;
    --band: #111213;
    --ink: #ffffff;
    --mesh-top: #7f95bf;
    --mesh-mid: #4f78b0;
    --mesh-low: #3f86a6;
    --mesh-foot: #58b7a8;
  }
  * { margin: 0; padding: 0; box-sizing: border-box; }
  html, body {
    width: 1200px; height: 900px; overflow: hidden;
    background: var(--stage);
    font-family: "Montserrat", sans-serif;
  }
  .canvas { position: relative; width: 1200px; height: 900px; }

  .card {
    position: absolute; top: 322px;
    width: 524px; height: 312px;
    border-radius: 16px;
    background: linear-gradient(135deg, var(--metal-edge), var(--metal) 40%, var(--metal-edge) 70%, var(--metal));
    box-shadow: 0 12px 28px rgba(0,0,0,0.35);
    overflow: hidden;
  }
  .card--front { left: 54px; }
  .card--back { left: 626px; height: 308px; }

  .mesh {
    position: absolute;
    border-radius: 14px;
    background: linear-gradient(180deg, var(--mesh-top) 0%, var(--mesh-mid) 45%, var(--mesh-low) 78%, var(--mesh-foot) 100%);
    opacity: 0.85;
  }
  .card--front .mesh { left: 16px; top: 14px; width: 492px; height: 264px; }
  .card--back .mesh { left: 14px; top: 18px; width: 492px; height: 260px; }

  .band {
    position: absolute;
    background: linear-gradient(120deg, #1a1b1d, var(--band) 60%, #1c1d20);
  }
  .card--front .band { left: 16px; top: 92px; width: 302px; height: 112px; }
  .card--back .band { left: 204px; top: 97px; width: 302px; height: 109px; }

  .wordmark {
    position: absolute; inset: 0;
    color: var(--ink); font-weight: 500;
    white-space: nowrap;
  }
  .wordmark__name {
    position: absolute; left: 72px; top: 113px;
    font-size: 58px; line-height: 70px; letter-spacing: 0.5px;
  }
  .wordmark__initial {
    position: absolute; left: 338px; top: 82px;
    font-size: 104px; line-height: 120px;
  }
  .wordmark__tld {
    position: absolute; left: 404px; top: 170px;
    font-size: 15px; line-height: 18px; letter-spacing: 1px;
  }

  .tagline {
    position: absolute; left: 0; right: 0; top: 287px;
    text-align: center;
    font-size: 13.5px; font-weight: 500;
    color: var(--ink); letter-spacing: 0.2px;
  }

  .contact {
    position: absolute; left: 204px; top: 97px; width: 302px; height: 109px;
    color: var(--ink); text-align: center;
  }
  .contact__name {
    margin-top: 16px;
    font-size: 19px; font-weight: 600; letter-spacing: 4px;
  }
  .contact__line { font-size: 15.5px; font-weight: 400; line-height: 23px; }
  .contact__phone { margin-top: 9px; }
</style>
</head>
<body>
<main class="canvas">
  <section class="card card--front" aria-label="Card front">
    <div class="mesh" role="img" aria-label="Hexagonal cut-out mesh showing through the metal"></div>
    <div class="band"></div>
    <p class="wordmark" aria-label="CalderW.com"><span class="wordmark__name">Calder</span><span class="wordmark__initial">W</span><span class="wordmark__tld">.com</span></p>
    <p class="tagline">THE CALDER WORKS - A RISK TRANSFER COMPANY</p>
  </section>

  <section class="card card--back" aria-label="Card back">
    <div class="mesh" role="img" aria-label="Hexagonal cut-out mesh showing through the metal"></div>
    <div class="band"></div>
    <div class="contact">
      <p class="contact__name">DEREK M.</p>
      <p class="contact__line contact__phone">+00 123 456 789</p>
      <p class="contact__line">EMAIL@MAILBOX-EXAMPLE.NET</p>
    </div>
  </section>
</main>
</body>
</html>
```